BRIGHTDESK - Remote Tech Support Site

We are looking for a new very responsive and simple website for our brand Brightdesk.com - a remote technical support company.

This company supports customers Globally in different countries throughout Eur/ North America / South America / Asia etc (please keep this in mind and integrate into the idea).

Its important to us that the design is very explanatory, the customer should easily be able to figure out that we provide computer support right away ... I like one page responsive type designs as well without a bunch of menu items

Here are some similar sites we like - but still looking for a unique design that fits out brand "brightdesk" - I have upload also some layouts i like (but the designs are not important just the layouts), youll see it includes consumer business etc which is important.

VOLM.COM - I love how clean it is - nice and white easy to see everything

PLUMWIRE247.COM - also nice the layout and responsive one page design makes it easy to use

corvalfix.com - similar to plumwire design as well - you can get the idea im looking for between the two

You will notice those examples are much different then the attachments I added - again this is more of an idea for possible layouts .. attached is also the logo - could inspire color scheme / blue white black etc

Target Market(s)

Home consumers without computer knowledge , older age 45-65, small medium business ... computer repair - slow computers

Industry/Entity Type

Computer Repair

Logo Text

Brightdesk

Coding

Coded - Design and coding required

Number of Pages Required

1 page

Font styles to use
Sans Serif
Other font styles liked:
• your choice responsive

Colors

Designer to choose colors to be used in the design.

Requirements
Must have
• Clean - responsive - professional design - the name says it all - brightdesk
• CALL TO ACTIONS FOR "Get Help Now!" / "Learn More" etc
Nice to have
• We are looking for a new very responsive and simple website for our brand Brightdesk.com - a remote technical support company.
• This company supports customers Globally in different countries throughout Eur/ North America / South America / Asia etc (please keep this in mind and integrate into the idea).
• Its important to us that the design is very explanatory, the customer should easily be able to figure out that we provide computer support right away ... I like one page responsive type designs as well without a bunch of menu items
• Here are some similar sites we like - but still looking for a unique design that fits out brand "brightdesk" - I have upload also some layouts i like (but the designs are not important just the layouts), youll see it includes consumer business etc which is important.
• VOLM.COM - I love how clean it is - nice and white easy to see everything
• PLUMWIRE247.COM - also nice the layout and responsive one page design makes it easy to use
• corvalfix.com - similar to plumwire design as well - you can get the idea im looking for between the two
Should not have
• dark, packed page - bad small font -

```html
<!DOCTYPE html>
<html lang="en">
<head>
<meta charset="utf-8">
<title>Brightdesk – Remote Tech Support</title>
<link href="https://fonts.googleapis.com/css2?family=Open+Sans:wght@400;600;700;800&display=swap" rel="stylesheet">
<style>
:root{
  --blue:#1e8cf0;
  --blue-dark:#1677d6;
  --ink:#222831;
  --text:#555b63;
  --muted:#8a9099;
  --line:#e6e8eb;
  --soft:#f4f5f7;
  --white:#ffffff;
  --green:#5cb85c;
  --footer:#262a30;
}
*{box-sizing:border-box;margin:0;padding:0}
html,body{width:1200px;height:4215px;overflow:hidden}
body{font-family:"Open Sans",Arial,sans-serif;color:var(--text);background:var(--white);position:relative}
.section{position:relative;width:1200px;overflow:hidden}
.abs{position:absolute}

/* Hero */
.hero{height:675px}
.hero-photo{position:absolute;inset:0;background:linear-gradient(100deg,#3c3a3c 0%,#5d5350 35%,#a28f85 60%,#c9b8ad 80%,#8c8c92 100%)}
.hero-shade{position:absolute;inset:0;background:linear-gradient(90deg,rgba(20,20,24,.55) 0%,rgba(20,20,24,.25) 45%,rgba(0,0,0,0) 70%)}
.topbar{position:absolute;top:0;left:0;width:1200px;height:45px;font-size:12px;color:var(--white)}
.topbar .contact{position:absolute;left:60px;top:15px;display:flex;gap:28px}
.topbar .contact span{display:flex;align-items:center;gap:7px}
.topbar .lang{position:absolute;right:178px;top:15px;display:flex;align-items:center;gap:6px}
.topbar .lang i{display:inline-block;width:16px;height:10px;background:#d9dde3;border-radius:1px}
.btn-login{position:absolute;right:58px;top:8px;width:100px;height:30px;border-radius:15px;background:var(--blue);color:var(--white);font-size:12px;font-weight:600;display:flex;align-items:center;justify-content:center}
.hero-copy{position:absolute;left:242px;top:232px;color:var(--white)}
.hero-copy h1{font-size:40px;font-weight:700;line-height:1.1}
.hero-copy h2{font-size:27px;font-weight:600;margin-top:6px}
.hero-copy p{font-size:14px;line-height:1.45;width:470px;margin-top:16px;opacity:.92}
.btn-ghost{display:inline-flex;align-items:center;justify-content:center;margin-top:22px;width:158px;height:46px;border:2px solid var(--white);border-radius:23px;color:var(--white);font-weight:700;font-size:16px}

/* Nav */
.nav{height:62px;background:var(--blue);color:var(--white)}
.brand{position:absolute;left:247px;top:16px;display:flex;align-items:center;gap:8px;font-size:22px;font-weight:600;letter-spacing:.2px}
.brand i{display:inline-block;width:28px;height:28px;border-radius:50%;background:var(--white)}
.menu{position:absolute;right:245px;top:23px;display:flex;gap:30px;font-size:12px;font-weight:700}

/* About */
.about{height:345px}
.sec-title-left{font-size:22px;font-weight:700;color:var(--ink)}
.about .sec-title-left{position:absolute;left:245px;top:54px}
.about-text{position:absolute;left:245px;top:102px;width:250px;font-size:12px;line-height:1.5}
.about-text p+p{margin-top:14px}
.promise{position:absolute;top:112px;width:160px;text-align:center}
.promise svg{display:block;margin:0 auto}
.promise h3{font-size:13px;font-weight:700;color:var(--ink);margin-top:14px}
.promise p{font-size:11px;color:var(--muted);line-height:1.5;margin-top:12px}

/* Real-time */
.realtime{height:408px;background:var(--white)}
.rt-photo{position:absolute;left:540px;top:0;width:660px;height:408px;background:linear-gradient(90deg,#ffffff 0%,#e3d8d2 25%,#b69a88 55%,#8c7465 80%,#5c5554 100%)}
.rt-copy{position:absolute;left:245px;top:42px}
.rt-copy h2{font-size:26px;font-weight:700;color:var(--ink);line-height:1.25}
.checks{list-style:none;margin-top:30px}
.checks li{display:flex;align-items:center;gap:12px;font-size:14px;margin-bottom:16px}
.btn-solid{display:inline-flex;align-items:center;justify-content:center;background:var(--blue);color:var(--white);font-weight:700;border-radius:22px}
.rt-copy .btn-solid{width:136px;height:42px;font-size:15px;margin-top:30px}

/* Features */
.features{height:477px}
.sec-title{position:absolute;left:0;width:1200px;text-align:center;font-size:22px;font-weight:700;color:var(--ink)}
.features .sec-title{top:52px}
.feature-grid{position:absolute;left:245px;top:112px;width:710px;display:grid;grid-template-columns:repeat(4,1fr);row-gap:30px}
.feature{padding:12px 14px 16px 0;border-right:1px solid var(--line);height:140px}
.feature:nth-child(4n){border-right:none}
.feature:not(:nth-child(4n+1)){padding-left:14px}
.feature svg{display:block}
.feature h3{font-size:14px;font-weight:600;color:var(--ink);margin-top:14px}
.feature p{font-size:11px;line-height:1.5;color:var(--muted);margin-top:6px}

/* Video */
.video{height:219px}
.video-photo{position:absolute;inset:0;background:linear-gradient(100deg,#2f7fd6 0%,#4b97e6 35%,#3a86da 65%,#256fc4 100%)}
.video-play{position:absolute;left:0;width:1200px;top:70px;text-align:center;color:var(--white)}
.video-play p{font-size:15px;font-weight:700;margin-top:10px}

/* Plans */
.plans{height:562px}
.plans .sec-title{top:56px}
.plan{position:absolute;top:135px;width:219px;background:var(--white);box-shadow:0 2px 10px rgba(0,0,0,.08);text-align:center}
.plan.featured{top:129px;box-shadow:0 8px 28px rgba(0,0,0,.18);padding-bottom:6px}
.plan-head{background:var(--blue);color:var(--white);height:44px;display:flex;align-items:center;justify-content:center;font-size:13px;font-weight:700}
.plan-price{font-size:22px;font-weight:700;color:var(--ink);margin-top:22px}
.plan-note{font-size:9px;color:var(--muted);margin-top:2px}
.plan-rule{width:52px;height:3px;background:var(--blue);margin:16px auto 22px}
.plan-row{font-size:10px;font-weight:600;color:var(--ink);height:33px;display:flex;align-items:center;justify-content:center}
.plan-row:nth-of-type(odd){background:var(--soft)}
.btn-outline{display:inline-flex;align-items:center;justify-content:center;width:116px;height:30px;border:1px solid var(--blue);color:var(--blue);border-radius:15px;font-size:11px;margin:20px 0 22px}
.plan .btn-solid{width:116px;height:30px;font-size:11px;margin:20px 0 22px}

/* Subscribe */
.subscribe{height:236px;background:var(--blue);color:var(--white);text-align:center}
.subscribe h2{font-size:22px;font-weight:700;padding-top:48px}
.subscribe p{font-size:11px;line-height:1.5;width:460px;margin:8px auto 0;opacity:.9}
.sub-form{position:absolute;left:365px;top:134px;width:470px;height:36px;border:1px solid rgba(255,255,255,.85);border-radius:18px;text-align:left}
.sub-form span{position:absolute;left:18px;top:10px;font-size:11px}
.sub-form b{position:absolute;right:2px;top:2px;width:106px;height:30px;border-radius:15px;background:var(--white);color:var(--blue);font-size:11px;display:flex;align-items:center;justify-content:center;font-weight:600}

/* Customers */
.customers{height:248px}
.customers .sec-title-left{position:absolute;left:245px;top:72px}
.cust-text{position:absolute;left:245px;top:122px;width:220px;font-size:10px;line-height:1.5;color:var(--muted)}
.quote{position:absolute;top:104px;width:226px;height:112px;background:var(--white);box-shadow:0 3px 14px rgba(0,0,0,.1);padding:10px 14px}
.quote .mark{font-size:28px;font-weight:800;color:var(--blue);line-height:.8}
.quote p{font-size:10px;line-height:1.5;color:var(--muted);margin-top:2px}
.quote h4{font-size:12px;font-weight:700;color:var(--ink);margin-top:10px}
.dots{position:absolute;left:490px;top:236px;display:flex;gap:5px}
.dots i{width:8px;height:8px;border-radius:50%;border:1px solid var(--blue)}
.dots i:first-child{background:var(--blue)}

/* Stats */
.stats{height:253px}
.stat{position:absolute;top:42px;width:200px;text-align:center}
.stat strong{display:block;font-size:42px;font-weight:400;color:var(--blue);line-height:1}
.stat span{display:block;font-size:19px;font-weight:700;color:var(--ink);line-height:1.2;margin-top:4px}

/* Map + contact */
.locate{height:379px}
.map{position:absolute;inset:0;background:linear-gradient(135deg,#d6d8db 0%,#e6e7e9 40%,#d0d3d6 70%,#e2e3e5 100%)}
.contact-card{position:absolute;left:245px;top:28px;width:225px;height:309px;background:var(--white);box-shadow:0 4px 18px rgba(0,0,0,.15);padding:22px 16px}
.contact-card h2{font-size:20px;font-weight:700;color:var(--ink)}
.contact-card>p{font-size:9px;line-height:1.5;color:var(--muted);margin-top:12px}
.contact-card ul{list-style:none;margin-top:16px}
.contact-card li{display:flex;gap:8px;font-size:9px;line-height:1.45;color:var(--text);margin-bottom:9px}
.contact-card li svg{flex:none}
.socials{display:flex;gap:10px;justify-content:center;margin-top:18px}
.socials i{width:30px;height:30px;border-radius:50%;border:1px solid var(--blue)}

/* Form */
.message{height:295px}
.field{position:absolute;border:1px solid var(--line);font-size:10px;color:var(--muted);padding:9px 10px}
.btn-send{position:absolute;left:478px;top:208px;width:247px;height:32px;background:var(--blue);color:var(--white);font-size:12px;display:flex;align-items:center;justify-content:center}

/* Footer */
.footer{height:56px;background:var(--footer);color:#d8dbe0;font-size:11px;text-align:center;line-height:56px}
</style>
</head>
<body>

<header class="section hero">
  <div class="hero-photo" role="img" aria-label="Smiling support agent wearing a headset"></div>
  <div class="hero-shade"></div>
  <div class="topbar">
    <div class="contact">
      <span><svg width="13" height="10" viewBox="0 0 13 10"><rect x=".5" y=".5" width="12" height="9" fill="none" stroke="#fff"/><path d="M.5 .5l6 5 6-5" fill="none" stroke="#fff"/></svg>info@brightdesk.com</span>
      <span><svg width="11" height="11" viewBox="0 0 24 24"><path fill="#fff" d="M6.6 10.8a15 15 0 006.6 6.6l2.2-2.2c.3-.3.7-.4 1-.2 1.1.4 2.3.6 3.6.6.6 0 1 .4 1 1V20c0 .6-.4 1-1 1A17 17 0 013 4c0-.6.4-1 1-1h3.5c.6 0 1 .4 1 1 0 1.3.2 2.5.6 3.6.1.3 0 .7-.2 1z"/></svg>(888) 555-0142</span>
    </div>
    <div class="lang">En-Us <i></i></div>
    <div class="btn-login">Login</div>
  </div>
  <div class="hero-copy">
    <h1>Dedicated Support</h1>
    <h2>Anytime, Anywhere</h2>
    <p>Friendly experts fix slow computers, viruses and setup issues remotely, in your country and your language, day or night.</p>
    <span class="btn-ghost">Get Help Now!</span>
  </div>
</header>

<nav class="section nav">
  <div class="brand"><i></i>brightdesk</div>
  <div class="menu"><span>HOME</span><span>ABOUT US</span><span>SERVICES</span><span>CONTACT US</span><span>FAQS</span></div>
</nav>

<section class="section about">
  <h2 class="sec-title-left">ABOUT US</h2>
  <div class="about-text">
    <p>Our team is a leader in providing top notch quality services and products with a focus on our customers' needs. We are happy to discuss your computer issues and provide a free remote diagnosis to determine the best solutions.</p>
    <p>While you are looking for the best source out there, we have everything for your computer and internet security!</p>
  </div>
  <div class="promise" style="left:462px">
    <svg width="44" height="38" viewBox="0 0 44 38"><rect x="2" y="9" width="40" height="27" rx="3" fill="none" stroke="#1e8cf0" stroke-width="2.5"/><path d="M15 9V4h14v5M2 19h40M19 19v4h6v-4" fill="none" stroke="#1e8cf0" stroke-width="2.5"/></svg>
    <h3>Free Diagnostic</h3>
    <p>Get a diagnostic from our tech for a completely free of charge.</p>
  </div>
  <div class="promise" style="left:640px">
    <svg width="46" height="36" viewBox="0 0 46 36"><rect x="7" y="3" width="32" height="23" rx="2" fill="none" stroke="#1e8cf0" stroke-width="2.5"/><path d="M2 31h42" stroke="#1e8cf0" stroke-width="3" stroke-linecap="round"/></svg>
    <h3>Get Fixed</h3>
    <p>Get fixed remotely, our certified tech will solve your issue fast.</p>
  </div>
  <div class="promise" style="left:814px">
    <svg width="46" height="38" viewBox="0 0 46 38"><path d="M12 30H10a8 8 0 010-16 12 12 0 0123-3 9 9 0 013 19h-2" fill="none" stroke="#1e8cf0" stroke-width="2.5"/><path d="M23 34V18m-6 6l6-6 6 6" fill="none" stroke="#1e8cf0" stroke-width="2.5"/></svg>
    <h3>Backup your Infos</h3>
    <p>Saving your files is key! You will be able to restore your data anytime.</p>
  </div>
</section>

<section class="section realtime">
  <div class="rt-photo" role="img" aria-label="Smiling woman looking down at her laptop"></div>
  <div class="rt-copy">
    <h2>Real-Time<br>Support Features &amp; Benifits</h2>
    <ul class="checks">
      <li><svg width="16" height="16" viewBox="0 0 16 16"><circle cx="8" cy="8" r="8" fill="#5cb85c"/><path d="M4.5 8.2l2.3 2.3 4.7-4.7" fill="none" stroke="#fff" stroke-width="1.8"/></svg>24/7 Real-Time Technician Support</li>
      <li><svg width="16" height="16" viewBox="0 0 16 16"><circle cx="8" cy="8" r="8" fill="#5cb85c"/><path d="M4.5 8.2l2.3 2.3 4.7-4.7" fill="none" stroke="#fff" stroke-width="1.8"/></svg>The Best Security Software in the market</li>
      <li><svg width="16" height="16" viewBox="0 0 16 16"><circle cx="8" cy="8" r="8" fill="#5cb85c"/><path d="M4.5 8.2l2.3 2.3 4.7-4.7" fill="none" stroke="#fff" stroke-width="1.8"/></svg>Regular Cleanups and optimization</li>
      <li><svg width="16" height="16" viewBox="0 0 16 16"><circle cx="8" cy="8" r="8" fill="#5cb85c"/><path d="M4.5 8.2l2.3 2.3 4.7-4.7" fill="none" stroke="#fff" stroke-width="1.8"/></svg>Setup and installation included</li>
    </ul>
    <span class="btn-solid">Learn More</span>
  </div>
</section>

<section class="section features">
  <h2 class="sec-title">Our Features</h2>
  <div class="feature-grid">
    <div class="feature"><svg width="22" height="22" viewBox="0 0 22 22"><rect x="4" y="9" width="14" height="11" rx="1" fill="none" stroke="#1e8cf0" stroke-width="1.6"/><path d="M7 9V6a4 4 0 018 0v3" fill="none" stroke="#1e8cf0" stroke-width="1.6"/></svg><h3>Ad Blocker</h3><p>Avoid unwanted Pop-ups with the newest Ad Blocking technology.</p></div>
    <div class="feature"><svg width="22" height="22" viewBox="0 0 22 22"><rect x="2" y="4" width="18" height="12" rx="1" fill="none" stroke="#1e8cf0" stroke-width="1.6"/><path d="M7 20h8M11 16v4" stroke="#1e8cf0" stroke-width="1.6"/></svg><h3>Regular Tune-Ups</h3><p>Avoid unwanted Pop-ups with the newest Ad Blocking technology.</p></div>
    <div class="feature"><svg width="22" height="22" viewBox="0 0 22 22"><rect x="3" y="3" width="16" height="16" rx="1" fill="none" stroke="#1e8cf0" stroke-width="1.6"/><path d="M3 8h16M8 8v11" stroke="#1e8cf0" stroke-width="1.6"/></svg><h3>System Reports</h3><p>Avoid unwanted Pop-ups with the newest Ad Blocking technology.</p></div>
    <div class="feature"><svg width="22" height="22" viewBox="0 0 22 22"><rect x="2" y="3" width="14" height="11" rx="1" fill="none" stroke="#1e8cf0" stroke-width="1.6"/><rect x="13" y="9" width="7" height="11" rx="1" fill="#fff" stroke="#1e8cf0" stroke-width="1.6"/></svg><h3>Multiple Devices</h3><p>Avoid unwanted Pop-ups with the newest Ad Blocking technology.</p></div>
    <div class="feature"><svg width="22" height="22" viewBox="0 0 22 22"><rect x="3" y="4" width="16" height="14" rx="1" fill="none" stroke="#1e8cf0" stroke-width="1.6"/><circle cx="9" cy="10" r="2.5" fill="none" stroke="#1e8cf0" stroke-width="1.4"/><path d="M13 9h4M13 13h4" stroke="#1e8cf0" stroke-width="1.4"/></svg><h3>Identity Protection</h3><p>Avoid unwanted Pop-ups with the newest Ad Blocking technology.</p></div>
    <div class="feature"><svg width="22" height="22" viewBox="0 0 22 22"><rect x="6" y="2" width="10" height="18" rx="2" fill="none" stroke="#1e8cf0" stroke-width="1.6"/><path d="M10 17h2" stroke="#1e8cf0" stroke-width="1.6"/></svg><h3>Mobile Security</h3><p>Avoid unwanted Pop-ups with the newest Ad Blocking technology.</p></div>
    <div class="feature"><svg width="22" height="22" viewBox="0 0 22 22"><rect x="2" y="4" width="12" height="9" rx="1" fill="none" stroke="#1e8cf0" stroke-width="1.6"/><rect x="9" y="10" width="11" height="8" rx="1" fill="#fff" stroke="#1e8cf0" stroke-width="1.6"/></svg><h3>Cross Platform Support</h3><p>Avoid unwanted Pop-ups with the newest Ad Blocking technology.</p></div>
    <div class="feature"><svg width="22" height="22" viewBox="0 0 22 22"><path d="M6 17H5a4 4 0 010-8 6 6 0 0111-2 4.5 4.5 0 011 9" fill="none" stroke="#1e8cf0" stroke-width="1.6"/></svg><h3>Cloud Backup</h3><p>Avoid unwanted Pop-ups with the newest Ad Blocking technology.</p></div>
  </div>
</section>

<section class="section video">
  <div class="video-photo" role="img" aria-label="Blue-tinted still of a technician helping a customer"></div>
  <div class="video-play">
    <svg width="46" height="46" viewBox="0 0 46 46"><rect x="2" y="2" width="42" height="42" rx="6" fill="none" stroke="#fff" stroke-width="2.5"/><path d="M18 13l14 10-14 10z" fill="#fff"/></svg>
    <p>Play Video</p>
  </div>
</section>

<section class="section plans">
  <h2 class="sec-title">Our Plans</h2>
  <div class="plan" style="left:245px">
    <div class="plan-head">PREMIUM</div>
    <div class="plan-price">$19.99 / MONTH</div>
    <div class="plan-note">(Billed yearly, no setup fee)</div>
    <div class="plan-rule"></div>
    <div class="plan-row">Regular 30-Day Optimization</div>
    <div class="plan-row">Unlimited 24/7 Tier 3</div>
    <div class="plan-row">Technician Support</div>
    <span class="btn-outline">Learn More</span>
  </div>
  <div class="plan featured" style="left:489px">
    <div class="plan-head">PLATINUM</div>
    <div class="plan-price">$39.99 / MONTH</div>
    <div class="plan-note">(Billed yearly, no setup fee)</div>
    <div class="plan-rule"></div>
    <div class="plan-row">Regular 30-Day Optimization</div>
    <div class="plan-row">Unlimited 24/7 Tier 3</div>
    <div class="plan-row">Technician Support</div>
    <div class="plan-row">Online Identity Theft Protection</div>
    <span class="btn-solid">Learn More</span>
  </div>
  <div class="plan" style="left:736px">
    <div class="plan-head">PREMIUM PLUS</div>
    <div class="plan-price">$29.99 / MONTH</div>
    <div class="plan-note">(Billed yearly, no setup fee)</div>
    <div class="plan-rule"></div>
    <div class="plan-row">Regular 30-Day Optimization</div>
    <div class="plan-row">Unlimited 24/7 Tier 3</div>
    <div class="plan-row">Technician Support</div>
    <span class="btn-outline">Learn More</span>
  </div>
</section>

<section class="section subscribe">
  <h2>Subscribe Us</h2>
  <p>Get security tips, software news and special offers from our team delivered straight to your inbox every month.</p>
  <div class="sub-form"><span>Email Id</span><b>Subscribe</b></div>
</section>

<section class="section customers">
  <h2 class="sec-title-left">Our Customers</h2>
  <p class="cust-text">Thousands of homes and small businesses across Europe, the Americas and Asia trust us to keep their computers fast, safe and running. Read what a few of them have to say about the help they received from our friendly team.</p>
  <div class="quote" style="left:487px"><div class="mark">“</div><p>My old laptop was painfully slow. The technician cleaned it up remotely in under an hour and explained every step clearly.</p><h4>Alex Doe</h4></div>
  <div class="quote" style="left:731px"><div class="mark">“</div><p>Our small office relies on their support plan. Whenever something breaks, help is only a phone call away.</p><h4>Alan Hue</h4></div>
  <div class="dots"><i></i><i></i><i></i></div>
</section>

<section class="section stats">
  <div class="stat" style="left:232px"><strong>25000</strong><span>Customers</span></div>
  <div class="stat" style="left:411px"><strong>750</strong><span>Employees</span></div>
  <div class="stat" style="left:594px"><strong>65000</strong><span>Computers<br>Repaired</span></div>
  <div class="stat" style="left:777px"><strong>2</strong><span>Business<br>done</span></div>
</section>

<section class="section locate">
  <div class="map" role="img" aria-label="Street map of the office location downtown"></div>
  <div class="contact-card">
    <h2>Get in touch</h2>
    <p>Reach our support team any time by phone, email or the form below, we answer quickly.</p>
    <ul>
      <li><svg width="10" height="12" viewBox="0 0 10 12"><path d="M5 0a4 4 0 014 4c0 3-4 8-4 8S1 7 1 4a4 4 0 014-4z" fill="#1e8cf0"/><circle cx="5" cy="4" r="1.5" fill="#fff"/></svg>Northgate Ltd, 210 Harbour St,<br>Halifax, NS B3J 1A1 Canada</li>
      <li><svg width="10" height="10" viewBox="0 0 24 24"><path fill="#1e8cf0" d="M6.6 10.8a15 15 0 006.6 6.6l2.2-2.2c.3-.3.7-.4 1-.2 1.1.4 2.3.6 3.6.6.6 0 1 .4 1 1V20c0 .6-.4 1-1 1A17 17 0 013 4c0-.6.4-1 1-1h3.5c.6 0 1 .4 1 1 0 1.3.2 2.5.6 3.6.1.3 0 .7-.2 1z"/></svg>(888) 555-0142</li>
      <li><svg width="11" height="9" viewBox="0 0 13 10"><rect x=".5" y=".5" width="12" height="9" fill="none" stroke="#1e8cf0"/><path d="M.5 .5l6 5 6-5" fill="none" stroke="#1e8cf0"/></svg>info@brightdesk.com</li>
    </ul>
    <div class="socials"><i></i><i></i></div>
  </div>
</section>

<section class="section message">
  <div class="field" style="left:245px;top:56px;width:345px;height:30px">Name</div>
  <div class="field" style="left:610px;top:56px;width:345px;height:30px">Email</div>
  <div class="field" style="left:245px;top:100px;width:710px;height:90px">Message</div>
  <div class="btn-send">Send Message</div>
</section>

<footer class="section footer">Brightdesk © 2016. All Rights Reserved. Terms and Conditions - Refund Policy - Privacy Policy.</footer>

</body>
</html>
```